Velvet Orchard - R&B Band in Sydney Requires new Business Cards

We're a 6 piece R&B Soul band in Sydney called Velvet Orchard that requires new promotional material including Business Cards.

We are very well known around Sydney and have a resident venue gig at the Marlowe Sydney hotel. We play predominantly old & new school R&B hits.

Our logo is attached, colours are Brown & yellow.
Initial idea was to get sugar packets made up with our logo and contact details.

```html
<!DOCTYPE html>
<html lang="en">
<head>
<meta charset="utf-8">
<title>Velvet Orchard – Business Cards</title>
<link href="https://fonts.googleapis.com/css2?family=Titan+One&family=Pacifico&family=Lato:wght@700&display=swap" rel="stylesheet">
<style>
  :root {
    --page: #ece8df;
    --brown: #3a2a10;
    --brown-deep: #2b1d08;
    --yellow: #f7e628;
    --yellow-soft: #fdf16a;
  }
  * { margin: 0; padding: 0; box-sizing: border-box; }
  html, body {
    width: 1200px;
    height: 576px;
    overflow: hidden;
    background: var(--page);
  }
  .canvas {
    width: 1200px;
    height: 576px;
    display: flex;
    align-items: center;
    justify-content: center;
    gap: 60px;
  }
  .card {
    width: 520px;
    height: 300px;
    border-radius: 4px;
    position: relative;
    overflow: hidden;
    box-shadow: 0 6px 18px rgba(0,0,0,0.18);
  }
  /* back of card */
  .card--back {
    background: var(--brown);
    display: flex;
    align-items: center;
    justify-content: center;
  }
  .band-name {
    font-family: "Titan One", sans-serif;
    color: var(--yellow);
    font-size: 58px;
    line-height: 0.95;
    text-align: center;
    text-transform: uppercase;
    letter-spacing: 1px;
  }
  /* front of card */
  .card--front {
    background: linear-gradient(135deg, var(--yellow-soft) 0%, var(--yellow) 55%);
    color: var(--brown-deep);
  }
  .guitar-art {
    position: absolute;
    left: 34px;
    top: 40px;
    width: 150px;
    height: 58px;
    background: linear-gradient(90deg, #6b5420, var(--brown-deep));
    border-radius: 6px;
    transform: rotate(-18deg);
  }
  .contact {
    position: absolute;
    right: 34px;
    top: 30px;
    text-align: left;
  }
  .contact__name {
    font-family: "Titan One", sans-serif;
    font-size: 64px;
    line-height: 0.9;
    text-transform: uppercase;
  }
  .contact__role {
    font-family: "Titan One", sans-serif;
    font-size: 30px;
    line-height: 1.05;
    margin-top: 4px;
  }
  .contact__phone {
    font-family: "Titan One", sans-serif;
    font-size: 28px;
    line-height: 1.1;
    letter-spacing: 1px;
  }
  .contact__handle {
    font-family: "Pacifico", cursive;
    font-size: 20px;
    line-height: 1.4;
  }
  .contact__web {
    font-family: "Lato", sans-serif;
    font-weight: 700;
    font-size: 16px;
  }
</style>
</head>
<body>
  <main class="canvas">
    <section class="card card--back" aria-label="Card back">
      <p class="band-name">Velvet<br>Orchard</p>
    </section>

    <section class="card card--front" aria-label="Card front">
      <div class="guitar-art" role="img" aria-label="Illustration of an electric guitar"></div>
      <div class="contact">
        <h1 class="contact__name">Jamie<br>Reyes</h1>
        <p class="contact__role">guitarist</p>
        <p class="contact__phone">0400555018</p>
        <p class="contact__handle">@velvetorchard</p>
        <p class="contact__web">www.velvetorchard.com</p>
      </div>
    </section>
  </main>
</body>
</html>
```